Lumaro Feat Archive. The First Black Republic. 1 record - 1 cause

Design a modern fb page showcasing world records broken or to be broken in Haiti, encouraging peopple around the world to take part or support those initiaves.
Despite having gained victory over colonial powers and becoming the first black republic in 1804, Haiti is often reffered to with negative concepts.

Goal of this initiative is to shed a more positive ligh onbthis caribbean country by the means of breaking or setting world records.

The Social Media package should be a window and an invitation to be part of each record attempt.

Suggested usage:
On the left a stadium with people on the field forming the haitian flag.
Right of the stadium the new logo on top and underneath some text in 4 languages
On the right the statue on top and the forteresse under it
On the far right the cruise boat

All images blend smoothly into one another.

Of course you can play around and make suggestiins

Target Market(s)

Haitians and friends around the world

Industry/Entity Type

It Support

Font styles to use
Serif

Requirements
Must have
• integration of crowdfunding campaingns and website
Nice to have
• Expecting suggestions

```html
<!DOCTYPE html>
<html lang="en">
<head>
<meta charset="utf-8">
<title>Lumaro Feat Archive – Page</title>
<link rel="stylesheet" href="https://fonts.googleapis.com/css2?family=Arimo:wght@400;700&family=Fjalla+One&display=swap">
<style>
  :root{
    --bar-blue:#3d5a98;
    --page-bg:#e9ebee;
    --panel:#ffffff;
    --line:#dddfe2;
    --text:#4b4f56;
    --text-dark:#1d2129;
    --muted:#90949c;
    --link:#365899;
    --cta:#4080f0;
    --flag-blue:#0b2fa8;
    --flag-red:#d2102e;
    --slogan-gold:#fcd67f;
    --white:#ffffff;
    --nav-active:#dfe1e6;
  }
  *{box-sizing:border-box;margin:0;padding:0}
  html,body{width:1200px;height:585px;overflow:hidden}
  body{background:var(--page-bg);font-family:"Arimo",Helvetica,Arial,sans-serif;color:var(--text);position:relative}
  .abs{position:absolute}

  /* top bar */
  .topbar{left:0;top:0;width:1200px;height:43px;background:var(--bar-blue)}
  .brand{left:87px;top:7px;height:24px;display:flex;align-items:center;color:var(--white);font-weight:700;font-size:13px;gap:5px}
  .brand-dot{width:9px;height:9px;background:var(--white);border-radius:2px}
  .search{left:150px;top:7px;width:416px;height:24px;background:var(--white);border-radius:2px}
  .search-btn{right:0;top:0;width:46px;height:24px;background:#f6f7f9;border-left:1px solid var(--line);display:flex;align-items:center;justify-content:center}
  .user{left:754px;top:8px;display:flex;align-items:center;gap:7px;color:var(--white);font-weight:700;font-size:12px}
  .avatar-sm{width:22px;height:22px;background:linear-gradient(135deg,#6b4a32,#c89468);border-radius:2px}
  .divider{width:1px;height:18px;background:#2d4a86;margin:0 8px}
  .bar-icons{left:940px;top:10px;display:flex;gap:13px;align-items:center}

  /* profile */
  .profile{left:88px;top:54px;width:170px;height:168px;background:var(--panel);border:1px solid #cfd2d8;border-radius:3px;padding:5px}
  .profile-inner{width:100%;height:100%;position:relative;background:var(--white);border:1px solid #e5e5e5;display:flex;align-items:center;justify-content:center}
  .profile-name{text-align:center;font-family:"Fjalla One",sans-serif;color:var(--flag-blue);font-size:20px;line-height:24px;width:130px}

  /* cover */
  .cover{left:271px;top:43px;width:828px;height:314px;overflow:hidden;background:linear-gradient(180deg,var(--flag-blue) 0 50%,var(--flag-red) 50% 100%)}
  .stadium{left:0;top:0;width:330px;height:314px;
    background:linear-gradient(180deg,#2a2c33 0%,#3b3f4a 10%,#1f3fa0 30%,#2044b4 45%,#c01d35 60%,#8e2030 75%,#3a3436 100%);
    -webkit-mask-image:linear-gradient(90deg,#000 75%,transparent 100%);mask-image:linear-gradient(90deg,#000 75%,transparent 100%)}
  .scenery{left:540px;top:0;width:288px;height:314px;
    background:linear-gradient(180deg,#6f8fb4 0%,#9db7cf 25%,#b5c6d2 40%,#4f95b0 60%,#2ab3c7 75%,#d9c8a0 88%,#8aa060 100%);
    -webkit-mask-image:linear-gradient(90deg,transparent 0%,#000 30%);mask-image:linear-gradient(90deg,transparent 0%,#000 30%)}
  .cover-name{left:290px;top:92px;width:244px;text-align:center;font-family:"Fjalla One",sans-serif;color:var(--white);font-size:28px;line-height:34px}
  .slogans{left:302px;top:170px;font-family:"Fjalla One",sans-serif;color:var(--white)}
  .slogans p{white-space:nowrap}
  .s1{color:var(--slogan-gold);font-size:38px;line-height:44px}
  .s2{font-size:30px;line-height:31px}
  .s3{font-size:25px;line-height:31px}
  .s4{font-size:23.5px;line-height:27px}

  /* action row */
  .actions{left:271px;top:357px;width:828px;height:51px;background:var(--panel);border:1px solid var(--line);border-top:0}
  .btn-group{left:13px;top:12px;height:27px;display:flex;border:1px solid #ccd0d5;border-radius:2px;background:#f6f7f9}
  .btn{display:flex;align-items:center;gap:5px;padding:0 10px;font-size:12px;font-weight:700;color:var(--text);border-right:1px solid #ccd0d5}
  .btn:last-child{border-right:0}
  .caret{width:0;height:0;border-left:4px solid transparent;border-right:4px solid transparent;border-top:4px solid var(--text)}
  .contact{left:517px;top:12px;width:297px;height:27px;background:var(--cta);border-radius:2px;color:var(--white);font-size:14px;display:flex;align-items:center;justify-content:center}

  /* nav */
  .nav{left:87px;top:328px;width:176px}
  .nav li{list-style:none;height:32px;line-height:32px;padding-left:10px;font-size:14px;color:var(--text)}
  .nav li.active{background:var(--nav-active);border-left:3px solid var(--link);padding-left:7px;font-weight:700;color:var(--text-dark)}

  /* composer */
  .composer{left:271px;top:423px;width:502px;height:107px;background:var(--panel);border:1px solid var(--line);border-radius:3px}
  .composer-head{left:0;top:0;width:100%;height:32px;background:#f6f7f9;border-bottom:1px solid var(--line);display:flex;align-items:center;padding-left:18px;gap:6px;font-size:12px}
  .composer-head .status{color:var(--text-dark);margin-right:8px}
  .composer-head .photo{color:var(--link)}
  .audience{right:10px;top:8px;display:flex;align-items:center;gap:4px}
  .avatar-xs{width:15px;height:15px;background:linear-gradient(135deg,#6b4a32,#c89468)}
  .avatar-md{left:13px;top:45px;width:40px;height:40px;background:linear-gradient(135deg,#3c2a1e,#b58a62)}
  .prompt{left:64px;top:58px;font-size:14px;color:#a1849a}

  /* likes */
  .likes{left:788px;top:421px;width:311px;height:109px;background:var(--panel);border:1px solid var(--line);border-radius:3px}
  .likes-top{left:0;top:0;width:100%;height:57px;border-bottom:1px solid var(--line)}
  .avatar-like{left:6px;top:12px;width:34px;height:34px;background:linear-gradient(135deg,#7a5a3e,#e1c4a4)}
  .like-count{left:51px;top:14px;font-size:12px;color:var(--text)}
  .like-friends{left:51px;top:35px;font-size:12px;color:var(--muted)}
  .invite{left:53px;top:75px;font-size:12px;color:var(--text-dark)}
  .invite-icon{left:15px;top:72px}
</style>
</head>
<body>

<header class="abs topbar">
  <div class="abs brand"><span class="brand-dot"></span>Palvo</div>
  <div class="abs search">
    <div class="abs search-btn">
      <svg width="13" height="13" viewBox="0 0 13 13"><circle cx="5.5" cy="5.5" r="4" fill="none" stroke="#4b4f56" stroke-width="1.6"/><line x1="8.5" y1="8.5" x2="12" y2="12" stroke="#4b4f56" stroke-width="1.8"/></svg>
    </div>
  </div>
  <div class="abs user">
    <span class="avatar-sm" role="img" aria-label="User profile photo"></span>
    <span>Dorel Vance</span>
    <span class="divider"></span>
    <span>Home</span>
    <span class="divider"></span>
  </div>
  <div class="abs bar-icons">
    <svg width="20" height="18" viewBox="0 0 20 18" aria-label="Friend requests"><circle cx="7" cy="5" r="4" fill="#fff"/><path d="M0 17c0-5 3-7 7-7s7 2 7 7z" fill="#fff"/><circle cx="14" cy="4" r="3.2" fill="#fff"/><path d="M13 9c4 0 7 2 7 7h-4c0-3-1-5-3-7z" fill="#fff"/></svg>
    <svg width="20" height="18" viewBox="0 0 20 18" aria-label="Messages"><path d="M5 1h14v10h-3v3l-3-3H5z" fill="#fff"/><path d="M1 6h3v6h8v2H7l-3 3v-3H1z" fill="#fff"/></svg>
    <svg width="18" height="18" viewBox="0 0 18 18" aria-label="Notifications"><circle cx="9" cy="9" r="8.5" fill="#fff"/><path d="M5 4c2 1 1 3 3 3s1 3-1 4M11 2c0 2 2 2 3 4M12 12c1 1 2 1 3 0" stroke="#3d5a98" stroke-width="1.6" fill="none"/></svg>
    <span style="width:1px;height:18px;background:#2d4a86;margin:0 8px"></span>
    <svg width="16" height="14" viewBox="0 0 16 14" aria-label="Privacy"><rect x="1" y="5" width="9" height="8" fill="#23396b"/><path d="M3 5V3a2.5 2.5 0 0 1 5 0v2" fill="none" stroke="#23396b" stroke-width="1.6"/><rect x="11" y="6" width="5" height="1.6" fill="#23396b"/><rect x="11" y="9" width="5" height="1.6" fill="#23396b"/></svg>
    <svg width="10" height="6" viewBox="0 0 10 6"><path d="M0 0h10L5 6z" fill="#23396b"/></svg>
  </div>
</header>

<div class="abs profile">
  <div class="profile-inner">
    <div class="profile-name">Lumaro Feat Archive</div>
  </div>
</div>

<section class="abs cover">
  <div class="abs stadium" role="img" aria-label="Stadium crowd forming the national flag on the field"></div>
  <div class="abs scenery" role="img" aria-label="Statue, hilltop fortress, turquoise bay and cruise ship"></div>
  <div class="abs cover-name">Lumaro Feat Archive</div>
  <div class="abs slogans">
    <p class="s1">Ansanm Nou Fò</p>
    <p class="s2">L union fait la force</p>
    <p class="s3">Together We are Strong</p>
    <p class="s4">Juntos Somos Poderosos</p>
  </div>
</section>

<div class="abs actions">
  <div class="abs btn-group">
    <div class="btn">
      <svg width="13" height="12" viewBox="0 0 13 12"><rect x="0" y="5" width="3" height="7" fill="#4b4f56"/><path d="M4 5l3-5c1.5 0 2 1 1.5 2.5L8 4.5h4c1 0 1 1 1 1.5l-1.5 5.5H4z" fill="#4b4f56"/></svg>
      Liked <span class="caret"></span>
    </div>
    <div class="btn">
      <svg width="14" height="13" viewBox="0 0 14 13"><ellipse cx="7" cy="5.5" rx="7" ry="5.5" fill="#90949c"/><path d="M3 9l-1 4 4-2z" fill="#90949c"/></svg>
      Message
    </div>
    <div class="btn">
      <svg width="14" height="4" viewBox="0 0 14 4"><circle cx="2" cy="2" r="1.5" fill="#90949c"/><circle cx="7" cy="2" r="1.5" fill="#90949c"/><circle cx="12" cy="2" r="1.5" fill="#90949c"/></svg>
      More <span class="caret"></span>
    </div>
  </div>
  <div class="abs contact">Contact Us</div>
</div>

<ul class="abs nav">
  <li class="active">Home</li>
  <li>Photos</li>
  <li>Likes</li>
  <li>About</li>
  <li>Videos</li>
  <li>Welcome</li>
  <li>Posts</li>
</ul>

<section class="abs composer">
  <div class="abs composer-head">
    <svg width="16" height="16" viewBox="0 0 16 16"><path d="M2 14l1-4 8-8 3 3-8 8z" fill="#4267b2"/><path d="M2 14l1-4 3 3z" fill="#f7923b"/></svg>
    <span class="status">Status</span>
    <svg width="16" height="13" viewBox="0 0 16 13"><rect x="0" y="2" width="16" height="11" rx="1" fill="#90949c"/><circle cx="8" cy="7.5" r="3" fill="#fff"/><rect x="5" y="0" width="6" height="3" fill="#90949c"/></svg>
    <span class="photo">Photo / Video</span>
    <div class="abs audience">
      <span class="avatar-xs" role="img" aria-label="User photo"></span>
      <svg width="8" height="5" viewBox="0 0 8 5"><path d="M0 0h8L4 5z" fill="#4b4f56"/></svg>
    </div>
  </div>
  <div class="abs avatar-md" role="img" aria-label="User profile photo"></div>
  <p class="abs prompt">Hello!! When is the next camping trip you have?</p>
</section>

<aside class="abs likes">
  <div class="abs likes-top">
    <div class="abs avatar-like" role="img" aria-label="Friend profile photo"></div>
    <p class="abs like-count">67.341 people like this</p>
    <p class="abs like-friends">Dorel Vance and 37 other friends</p>
  </div>
  <svg class="abs invite-icon" width="20" height="16" viewBox="0 0 20 16"><circle cx="7" cy="4" r="4" fill="#bec2c9"/><path d="M0 16c0-5 3-7 7-7s7 2 7 7z" fill="#bec2c9"/><rect x="15" y="2" width="2" height="8" fill="#bec2c9"/><rect x="12" y="5" width="8" height="2" fill="#bec2c9"/></svg>
  <p class="abs invite">Invite friends to like this Page</p>
</aside>

</body>
</html>
```